Water ATM Card

Need a design for water ATM cards. Size of card is 3.375 x 2.125 inch
On the Front include the Cedar brook Logo.
Bottom right corner should have Price $100
On the Back
This card is to be used to access water refills at any Cedar Brook Water Vending Machines.
Please contact (869) 614 2938 or (869) 731 4072 or email clearflowhq@examplemail.com for any assistance or recharging of card.

```html
<!DOCTYPE html>
<html lang="en">
<head>
<meta charset="utf-8">
<title>Cedar Brook Water ATM Card</title>
<link href="https://fonts.googleapis.com/css2?family=Bebas+Neue&family=Montserrat:wght@600;700&display=swap" rel="stylesheet">
<style>
  :root {
    --backdrop: #d9dadc;
    --card: #ffffff;
    --ink: #111111;
    --brand-blue: #1a78c2;
    --brand-green: #4bae3f;
    --water-light: #e4eef9;
    --water-mid: #a9c6ea;
    --water-deep: #4f82c9;
  }
  * { box-sizing: border-box; margin: 0; padding: 0; }
  html, body {
    width: 1200px; height: 694px; overflow: hidden;
    background: var(--backdrop);
  }
  .canvas {
    position: relative; width: 1200px; height: 694px;
    display: flex; align-items: center; justify-content: center; gap: 40px;
  }
  .card {
    position: relative; width: 540px; height: 340px;
    background: var(--card); overflow: hidden;
    box-shadow: 0 6px 18px rgba(0,0,0,.18);
  }
  .water {
    position: absolute; left: 0; right: 0; bottom: 0; height: 50%;
    background: linear-gradient(to bottom, rgba(228,238,249,0) 0%, var(--water-light) 30%, var(--water-mid) 70%, var(--water-deep) 100%);
  }
  .brand {
    position: absolute; display: flex; align-items: center; gap: 10px;
    font-family: "Montserrat", sans-serif; font-weight: 700;
    color: var(--brand-blue); letter-spacing: 2px; white-space: nowrap;
  }
  .brand-dot {
    width: 26px; height: 26px; border-radius: 50%; background: var(--brand-green);
  }

  /* back */
  .back-heading {
    position: absolute; left: 22px; top: 20px; right: 20px;
    font-family: "Bebas Neue", sans-serif; font-size: 31px; line-height: 1.02;
    color: var(--ink); text-transform: uppercase;
  }
  .card-back .brand { left: 50%; top: 118px; transform: translateX(-50%); font-size: 32px; }
  .back-contact {
    position: absolute; left: 10px; right: 10px; top: 200px;
    font-family: "Montserrat", sans-serif; font-weight: 600;
    font-size: 17px; line-height: 1.35; text-align: center; color: var(--ink);
  }

  /* front */
  .title-pill {
    position: absolute; left: 26px; right: 26px; top: 30px; height: 50px;
    border-radius: 25px; background: var(--brand-blue);
    box-shadow: 5px 5px 0 var(--brand-green);
    display: flex; align-items: center; justify-content: center;
    font-family: "Bebas Neue", sans-serif; font-size: 40px; color: #fff;
    letter-spacing: .5px; padding-top: 4px;
  }
  .card-front .brand { left: 50%; top: 148px; transform: translateX(-50%); font-size: 36px; }
  .price {
    position: absolute; right: 24px; bottom: 104px;
    font-family: "Montserrat", sans-serif; font-weight: 700;
    font-size: 24px; color: var(--ink);
  }
</style>
</head>
<body>
<main class="canvas">

  <section class="card card-back">
    <div class="water" role="img" aria-label="Splashing clear blue water with bubbles"></div>
    <h2 class="back-heading">This card is to be used to access water refills<br>at any Cedar Brook water vending machines.</h2>
    <div class="brand"><span class="brand-dot"></span>CEDAR BROOK</div>
    <p class="back-contact">
      Contact (869) 614 2938 or (869) 731 4072<br>
      or email clearflowhq@examplemail.com<br>
      for any assistance or recharging of card.
    </p>
  </section>

  <section class="card card-front">
    <div class="water" role="img" aria-label="Splashing clear blue water with bubbles"></div>
    <h1 class="title-pill">Cedar Brook Water ATM Card</h1>
    <div class="brand"><span class="brand-dot"></span>CEDAR BROOK</div>
    <p class="price">Price $100</p>
  </section>

</main>
</body>
</html>
```